Halvorn spray foam and Environmental

I have business cards but need new ones. The ones I have are very bland. Here is. Y company website http://www.halvornsprayfoam.ca

Also I can send you copies of the current cards
I would also need my current logo on the new design as well.. Also spray foam and Environmental

Industry/Entity Type

Business

Logo Text

Halvorn.

```html
<!DOCTYPE html>
<html lang="en">
<head>
<meta charset="utf-8">
<title>Halvorn Spray Foam and Environmental – Business Card</title>
<link rel="stylesheet" href="https://fonts.googleapis.com/css2?family=Roboto:wght@400;500;700&family=Tinos&display=swap">
<style>
  :root {
    --page: #e9e6e3;
    --card-light: #f9f2fa;
    --purple: #4e2566;
    --purple-soft: #8a5aa8;
    --charcoal: #2d2d30;
    --slate: #4a4c55;
    --rule-grey: #c9c9cc;
    --muted: #a9a9ae;
    --text-purple: #5b3478;
    --icon-green: #4caf50;
    --white: #ffffff;
  }
  * { box-sizing: border-box; margin: 0; padding: 0; }
  html, body { width: 1200px; height: 675px; overflow: hidden; }
  body {
    background: var(--page);
    font-family: "Roboto", Arial, sans-serif;
    position: relative;
  }
  .card {
    position: absolute;
    left: 370px;
    width: 460px;
    height: 262px;
    overflow: hidden;
    box-shadow: 0 2px 6px rgba(0,0,0,.18);
  }
  /* Front */
  .card-front { top: 52px; background: var(--card-light); }
  .accent-bars { position: absolute; left: 0; top: 33px; }
  .accent-bars span { display: block; height: 4px; background: var(--purple); margin-bottom: 2px; }
  .accent-bars span:nth-child(1) { width: 45px; }
  .accent-bars span:nth-child(2) { width: 40px; }
  .accent-bars span:nth-child(3) { width: 35px; }
  .brand {
    position: absolute; left: 0; right: 0; top: 84px;
    text-align: center;
  }
  .brand-mark {
    display: inline-block; width: 30px; height: 28px;
    background: var(--slate); margin-bottom: 6px;
  }
  .brand-name {
    font-weight: 700; font-size: 14px; letter-spacing: .3px;
    color: var(--purple); line-height: 1;
  }
  .brand-rule {
    width: 130px; height: 1px; margin: 5px auto 4px;
    background: linear-gradient(90deg, transparent, var(--muted), transparent);
  }
  .brand-tagline { font-size: 9.5px; color: var(--text-purple); }
  .front-rule {
    position: absolute; left: 0; right: 0; top: 218px;
    height: 3px; background: var(--purple);
  }
  /* Back */
  .card-back { top: 322px; background: var(--white); }
  .back-top {
    position: absolute; left: 0; right: 0; top: 0; height: 164px;
    background: var(--charcoal);
  }
  .back-name {
    position: absolute; left: 40px; top: 34px;
    font-size: 10px; font-weight: 500; color: var(--purple-soft);
  }
  .back-address {
    position: absolute; left: 40px; top: 48px;
    font-family: "Tinos", "Times New Roman", serif;
    font-size: 6.5px; line-height: 8px; color: var(--muted);
  }
  .back-brand {
    position: absolute; left: 185px; top: 68px;
    width: 78px; height: 60px;
    display: flex; align-items: center; justify-content: center;
    background: var(--slate);
    color: var(--white); font-size: 11px; font-weight: 700; letter-spacing: .4px;
  }
  .back-band-rule {
    position: absolute; left: 0; right: 0; top: 164px;
    height: 3px; background: var(--purple);
  }
  .contact {
    position: absolute; top: 172px;
  }
  .contact-foam { left: 36px; }
  .contact-enviro { left: 300px; }
  .contact-label {
    display: inline-block; background: var(--purple); color: var(--white);
    font-size: 9px; font-weight: 500; padding: 2px 9px; border-radius: 8px;
    margin-bottom: 4px;
  }
  .contact-list { list-style: none; }
  .contact-list li {
    display: flex; align-items: center; gap: 4px;
    font-size: 8px; color: var(--text-purple); line-height: 12px;
  }
  .contact-list svg { width: 8px; height: 8px; flex: none; }
  .back-bottom-rule {
    position: absolute; left: 0; right: 0; top: 234px;
    height: 4px; background: var(--rule-grey);
  }
  .back-bottom {
    position: absolute; left: 0; right: 0; top: 238px; bottom: 0;
    background: var(--slate);
  }
</style>
</head>
<body>
  <section class="card card-front" aria-label="Business card front">
    <div class="accent-bars"><span></span><span></span><span></span></div>
    <div class="brand">
      <span class="brand-mark"></span>
      <div class="brand-name">HALVORN</div>
      <div class="brand-rule"></div>
      <div class="brand-tagline">Spray Foam and Environmental</div>
    </div>
    <div class="front-rule"></div>
  </section>

  <section class="card card-back" aria-label="Business card back">
    <div class="back-top">
      <div class="back-name">HALVORN</div>
      <div class="back-address">4280 Alder Way Burnaby,<br>British Columbia v5x 2k4, CA</div>
      <div class="back-brand">HALVORN</div>
    </div>
    <div class="back-band-rule"></div>

    <div class="contact contact-foam">
      <span class="contact-label">Spray Foam</span>
      <ul class="contact-list">
        <li><svg viewBox="0 0 8 8"><rect width="8" height="8" rx="1" fill="var(--icon-green)"/><path d="M1 2.2 4 4.6 7 2.2" stroke="#fff" stroke-width=".9" fill="none"/></svg>halvornfoam@halvornmail.ca</li>
        <li><svg viewBox="0 0 8 8"><rect width="8" height="8" rx="1" fill="var(--icon-green)"/><path d="M2.3 1.5c.5 2 1.6 3.6 3.8 4.8" stroke="#fff" stroke-width="1.1" fill="none" stroke-linecap="round"/></svg>604-555-0148</li>
        <li><svg viewBox="0 0 8 8"><circle cx="4" cy="4" r="3.6" fill="var(--icon-green)"/><path d="M.6 4h6.8M4 .5c-1.8 2-1.8 5 0 7M4 .5c1.8 2 1.8 5 0 7" stroke="#fff" stroke-width=".6" fill="none"/></svg>www.halvornsprayfoam.ca</li>
      </ul>
    </div>

    <div class="contact contact-enviro">
      <span class="contact-label">Environmental</span>
      <ul class="contact-list">
        <li><svg viewBox="0 0 8 8"><rect width="8" height="8" rx="1" fill="var(--icon-green)"/><path d="M1 2.2 4 4.6 7 2.2" stroke="#fff" stroke-width=".9" fill="none"/></svg>halvornenviro@halvornmail.ca</li>
        <li><svg viewBox="0 0 8 8"><rect width="8" height="8" rx="1" fill="var(--icon-green)"/><path d="M2.3 1.5c.5 2 1.6 3.6 3.8 4.8" stroke="#fff" stroke-width="1.1" fill="none" stroke-linecap="round"/></svg>604-555-0192</li>
        <li><svg viewBox="0 0 8 8"><circle cx="4" cy="4" r="3.6" fill="var(--icon-green)"/><path d="M.6 4h6.8M4 .5c-1.8 2-1.8 5 0 7M4 .5c1.8 2 1.8 5 0 7" stroke="#fff" stroke-width=".6" fill="none"/></svg>www.halvornenvironmental.ca</li>
      </ul>
    </div>

    <div class="back-bottom-rule"></div>
    <div class="back-bottom"></div>
  </section>
</body>
</html>
```